Determining number of boxes of planks of flooring for a room

Need a creative design of an infographic of a room with instructions on how to measure the room and use this measurement to determine how much flooring to order.
The floor planks come in boxes and each box has 36 planks. Each box covers 5 metre squared in total.
The intent of the infographic is to help inform the customer how many boxes they need to order for their room.
The infographic should match the style of flooring being sold (image provided) and the logo for the company (image provided).
A crude sketch of instructions to measure a room and determine the number of boxes is provided in a document attached with this brief. Need improvement to the steps mentioned in this document on the infographic created.

```html
<!DOCTYPE html>
<html lang="en">
<head>
<meta charset="utf-8">
<title>Self Adhesive Vinyl Planks – Estimating Guide</title>
<link href="https://fonts.googleapis.com/css2?family=Barlow:wght@400;500;600&family=Barlow+Semi+Condensed:wght@600;700&family=Architects+Daughter&display=swap" rel="stylesheet">
<style>
  :root{
    --cream:#f1e7d8;
    --ink:#5a5044;
    --ink-dark:#4a4138;
    --copper:#c27a35;
    --rule:#d2c2ab;
    --swatch-walnut:#5c4434;
    --swatch-ash:#e2e0dc;
    --swatch-oak:#e3b06e;
    --swatch-grey:#a9a39b;
  }
  *{margin:0;padding:0;box-sizing:border-box}
  html,body{width:1200px;height:675px;overflow:hidden;background:var(--cream)}
  .canvas{position:relative;width:1200px;height:675px;background:var(--cream);color:var(--ink);font-family:"Barlow",sans-serif}
  .abs{position:absolute}
  .hand{font-family:"Architects Daughter",cursive;color:var(--ink)}

  .title{left:54px;top:44px;font-family:"Barlow Semi Condensed",sans-serif;font-weight:700;font-size:43px;line-height:1;letter-spacing:.3px;color:var(--ink)}
  .subtitle{left:54px;top:92px;font-family:"Barlow Semi Condensed",sans-serif;font-weight:600;font-size:23px;line-height:1;color:var(--copper);letter-spacing:.4px}
  .rule{left:54px;width:816px;height:1px;background:var(--rule)}

  .step{width:68px;height:68px;border-radius:50%;background:var(--ink);color:var(--cream);display:flex;flex-direction:column;align-items:center;justify-content:center;font-family:"Architects Daughter",cursive;font-size:16px;line-height:18px;text-align:center}
  .step-label{width:260px;text-align:center;font-size:15px;letter-spacing:.5px;top:236px}

  .placeholder{border-radius:2px}
  .ph-measure{left:55px;top:290px;width:262px;height:190px;background:linear-gradient(135deg,#dcd7cf,#c9a86f 60%,#e1dcd4)}
  .ph-boxes{left:380px;top:294px;width:104px;height:158px;background:linear-gradient(160deg,#e1c593,#c69d5f)}
  .ph-truck{left:605px;top:288px;width:266px;height:92px;background:linear-gradient(90deg,#c2935c,#a87848 70%,#5a5044)}
  .ph-person{left:648px;top:402px;width:52px;height:160px;background:linear-gradient(180deg,#e6cfae,#b8803f 55%,#7a5a3a)}
  .ph-photo{left:893px;width:307px}

  .small{font-size:11px;letter-spacing:.3px;line-height:1.1}
  .formula{left:305px;top:488px;width:284px;text-align:center;font-size:11px;letter-spacing:.3px}
  .formula-box{left:325px;top:502px;width:250px;height:18px;background:var(--ink-dark);color:var(--cream);font-size:11px;display:flex;align-items:center;justify-content:center}
  .formula-note{left:300px;top:521px;width:269px;text-align:right;font-size:10.5px;line-height:12px;letter-spacing:.2px}
  .vline{width:1px;top:489px;height:60px;background:var(--rule)}

  .help{left:727px;top:438px;width:150px;font-size:10.5px;line-height:12.3px}
  .help p+p{margin-top:9px}

  .brand{left:54px;top:598px}
  .brand-name{font-family:"Barlow",sans-serif;font-weight:500;font-size:36px;line-height:1;letter-spacing:1px;color:var(--ink);display:flex;align-items:center;gap:10px}
  .brand-name .mark{width:22px;height:22px;background:var(--ink)}
  .brand-tag{font-size:9px;letter-spacing:3.6px;font-weight:600;margin-top:3px;margin-left:32px;color:var(--ink)}
  .divider{left:330px;top:598px;width:2px;height:46px;background:var(--ink)}
  .contact{left:345px;top:596px;font-size:12px;color:var(--ink)}
  .contact h3{font-family:"Barlow Semi Condensed",sans-serif;font-weight:600;font-size:13px;letter-spacing:.3px;margin-bottom:6px}
  .contact .row{display:flex;align-items:center;gap:6px;height:17px;font-size:11.5px}
  .swatch{width:19px;height:19px;border-radius:50%;top:598px;border:1px solid rgba(0,0,0,.15)}
  .swatch-caption{left:640px;top:624px;width:248px;text-align:center;font-size:10.5px;color:var(--ink)}
</style>
</head>
<body>
<div class="canvas">

  <h1 class="abs title">SELF ADHESIVE VINYL PLANKS</h1>
  <h2 class="abs subtitle">GUIDE TO ESTIMATING FLOOR PLANKS REQUIRED FOR A SPACE</h2>
  <div class="abs rule" style="top:125px"></div>

  <!-- steps -->
  <div class="abs step" style="left:136px;top:153px"><span>STEP</span><span>01</span></div>
  <div class="abs step" style="left:422px;top:153px"><span>STEP</span><span>02</span></div>
  <div class="abs step" style="left:704px;top:153px"><span>STEP</span><span>03</span></div>
  <svg class="abs" style="left:0;top:0" width="893" height="675" aria-hidden="true">
    <g stroke="#5a5044" stroke-width="1.6" fill="none">
      <line x1="218" y1="187" x2="402" y2="187"/>
      <path d="M400 183 L408 187 L400 191 Z" fill="#5a5044"/>
      <line x1="502" y1="187" x2="685" y2="187"/>
      <path d="M683 183 L691 187 L683 191 Z" fill="#5a5044"/>
      <!-- curve: floor area to formula -->
      <path d="M237 414 C 275 430, 272 485, 212 490"/>
      <path d="M216 485 L208 490 L216 495" />
      <!-- curve: pack note to formula -->
      <path d="M556 397 C 605 405, 610 460, 583 495" stroke="#c27a35"/>
      <path d="M580 488 L582 497 L589 491" stroke="#c27a35"/>
      <!-- pack callout -->
      <circle cx="485" cy="362" r="3.5" fill="#c27a35" stroke="none"/>
      <polyline points="488,362 514,362 514,374" stroke-width="1"/>
    </g>
  </svg>
  <div class="abs hand step-label" style="left:55px">MEASURE FLOOR AREA</div>
  <div class="abs hand step-label" style="left:332px">COMPUTE PACKS REQUIRED</div>
  <div class="abs hand step-label" style="left:608px">PLACE YOUR ORDER!</div>

  <!-- step 1 -->
  <div class="abs placeholder ph-measure" role="img" aria-label="Illustration of a worker with a ruler beside a floor area outline"></div>
  <div class="abs hand small" style="left:190px;top:296px">L (LENGTH)</div>
  <div class="abs hand small" style="left:264px;top:375px">W (WIDTH)</div>
  <div class="abs hand small" style="left:75px;top:485px;width:122px;text-align:right;line-height:16px">FLOOR AREA<br>= LENGTH (L) x (WIDTH)</div>

  <!-- step 2 -->
  <div class="abs placeholder ph-boxes" role="img" aria-label="Illustration of three stacked cardboard plank packs"></div>
  <div class="abs hand" style="left:501px;top:378px;font-size:11px;line-height:10px">1 PACK =<br>36pcs<br>planks</div>
  <div class="abs vline" style="left:303px"></div>
  <div class="abs vline" style="left:619px"></div>
  <div class="abs hand formula">TOTAL NUMBER OF PACKS = FLOOR AREA ÷ 5</div>
  <div class="abs hand formula-box">One pack of planks covers a total area of 5m²</div>
  <div class="abs hand formula-note">(ALWAYS ROUND OFF THE FIGURE TO THE<br>NEAREST NEXT WHOLE NUMBER WHEN AREA<br>COMPUTED GIVES A DECIMAL POINT)</div>

  <!-- step 3 -->
  <div class="abs placeholder ph-truck" role="img" aria-label="Illustration of a delivery truck with two movers carrying a pack"></div>
  <svg class="abs" style="left:605px;top:376px" width="266" height="4" aria-hidden="true"><line x1="0" y1="2" x2="266" y2="2" stroke="#5a5044" stroke-width="1.2"/></svg>
  <div class="abs placeholder ph-person" role="img" aria-label="Illustration of a puzzled customer scratching his head"></div>
  <svg class="abs" style="left:727px;top:418px" width="12" height="8" aria-hidden="true"><path d="M0 0 L12 0 L6 6 Z" fill="#5a5044"/></svg>
  <div class="abs hand help">
    <p>Incase you are unsure of your space estimate, or is not a regular rectangle/ square, we are here to help!</p>
    <p>Share a simple floor area sketch and send it to us, we will be able to work out the estimates for you.</p>
  </div>

  <div class="abs rule" style="top:574px"></div>

  <!-- footer -->
  <div class="abs brand">
    <div class="brand-name"><span class="mark"></span>CORVELLA</div>
    <div class="brand-tag">PREMIUM FLOORS AND TILES</div>
  </div>
  <div class="abs divider"></div>
  <div class="abs contact">
    <h3>FOR MORE INFORMATION CONTACT</h3>
    <div class="row">
      <svg width="11" height="11" viewBox="0 0 24 24" fill="none" stroke="#5a5044" stroke-width="2"><path d="M5 3h4l2 5-3 2a12 12 0 0 0 6 6l2-3 5 2v4a2 2 0 0 1-2 2A18 18 0 0 1 3 5a2 2 0 0 1 2-2z"/></svg>
      <span>+44 000 000 000</span>
    </div>
    <div class="row">
      <svg width="12" height="10" viewBox="0 0 24 18" fill="none" stroke="#5a5044" stroke-width="2"><rect x="1" y="1" width="22" height="16"/><path d="M1 1l11 9 11-9"/></svg>
      <span>info@corvella.co.uk</span>
    </div>
  </div>
  <div class="abs swatch" style="left:658px;background:var(--swatch-walnut)"></div>
  <div class="abs swatch" style="left:723px;background:var(--swatch-ash)"></div>
  <div class="abs swatch" style="left:787px;background:var(--swatch-oak)"></div>
  <div class="abs swatch" style="left:851px;background:var(--swatch-grey)"></div>
  <div class="abs swatch-caption">Offering a wide range of choices on Vinyl planks</div>

  <!-- photo column -->
  <div class="abs ph-photo" style="top:0;height:156px;background:linear-gradient(180deg,#2c3b3a 0%,#1f4a42 45%,#3a2a22 75%,#2a1d17 100%)" role="img" aria-label="Photo of a green velvet sofa on dark walnut vinyl planks"></div>
  <div class="abs ph-photo" style="top:168px;height:164px;background:linear-gradient(160deg,#e9e7e3 0%,#9a6c3f 30%,#c9c6c0 60%,#b7b3ad 100%)" role="img" aria-label="Photo of a wooden chair on light grey vinyl planks"></div>
  <div class="abs ph-photo" style="top:343px;height:164px;background:linear-gradient(180deg,#8f8b86 0%,#efece6 45%,#d39a55 70%,#c0853f 100%)" role="img" aria-label="Photo of a white door and dresser on oak vinyl planks"></div>
  <div class="abs ph-photo" style="top:519px;height:156px;background:linear-gradient(120deg,#e8e4dc 0%,#e2b742 35%,#7b7a78 55%,#c2272b 85%,#8a1c1f 100%)" role="img" aria-label="Photo of a bedroom with red throw on grey vinyl planks"></div>

</div>
</body>
</html>
```